I need a business card design for my streamora channel called The Plain Kettle Show. I make streamora cooking tutorials. I'd like the phrase " I'll see you next time, for my next meal" somewhere on the BC. The Streamora web address is www.streamora.example/user/PlainKettleShow
email - promos@zentaclip.example
Updates
I have just updated what i am looking for on the card. Thanks
Industry/Entity Type
Cooking
Contact Information for Business Card
The name of my business is The Plain Kettle Show. It's a Streamora channel & the url is https://www.streamora.example/user/PlainKettleShow
Am am a StreamOra partner.
My name is Marcus.
Logo Text
The Plain Kettle Show
Logo styles of interest
Pictorial/Combination Logo
Look and feel
Each slider illustrates characteristics of the customer's brand and the style your logo design should communicate.

```html
<!DOCTYPE html>
<html lang="en">
<head>
<meta charset="utf-8">
<title>Plain Kettle Show — Business Card</title>
<link rel="stylesheet" href="https://fonts.googleapis.com/css2?family=Open+Sans:wght@400;600;700&display=swap">
<style>
  :root {
    --backdrop: #efe9e1;
    --card-frame: #ffffff;
    --card-orange: #f79d21;
    --logo-tile: #fd9a05;
    --ink: #231f1a;
    --paper: #ffffff;
    --cake-tone-a: #e8543a;
    --cake-tone-b: #3b8fd1;
    --jelly-tone-a: #d8322a;
    --jelly-tone-b: #2a7a3a;
  }
  * { box-sizing: border-box; margin: 0; padding: 0; }
  html, body {
    width: 1068px; height: 1200px; overflow: hidden;
    background: var(--backdrop);
    font-family: "Open Sans", Arial, sans-serif;
    color: var(--ink);
  }
  .canvas { position: relative; width: 1068px; height: 1200px; }

  .card {
    position: absolute; left: 211px; width: 643px; height: 366px;
    background: var(--card-frame);
  }
  .card__face {
    position: absolute; inset: 15px;
    background: var(--card-orange);
  }
  .card--front { top: 214px; clip-path: polygon(0 0, 100% 0, 100% 78%, 92% 100%, 0 100%); }
  .card--front .card__face { clip-path: polygon(0 0, 100% 0, 100% 78%, 91.5% 100%, 0 100%); }
  .card--back { top: 609px; clip-path: polygon(0 0, 100% 0, 100% 100%, 9% 100%, 0 83%); }
  .card--back .card__face { clip-path: polygon(0 0, 100% 0, 100% 100%, 8.5% 100%, 0 83%); }

  .logo-tile { position: absolute; background: var(--logo-tile); }
  .card--front .logo-tile { left: 18px; top: 8px; width: 143px; height: 143px; }
  .card--back .logo-tile { left: 43px; top: 85px; width: 145px; height: 145px; }

  .brand-name { position: absolute; font-weight: 600; font-size: 28px; line-height: 1; white-space: nowrap; }
  .tagline { position: absolute; font-size: 20px; line-height: 1; white-space: nowrap; }
  .card--front .brand-name { left: 186px; top: 38px; }
  .card--front .tagline { left: 186px; top: 74px; }
  .card--back .brand-name { left: 211px; top: 130px; }
  .card--back .tagline { left: 211px; top: 168px; }

  .photo {
    position: absolute; width: 160px; height: 155px;
    background: var(--paper); padding: 7px;
    box-shadow: 0 3px 6px rgba(0,0,0,.25);
  }
  .photo__fill { width: 100%; height: 100%; }
  .photo--cake { left: 232px; top: 112px; transform: rotate(2deg); }
  .photo--cake .photo__fill { background: linear-gradient(160deg, var(--cake-tone-b), var(--cake-tone-a) 55%, #f2c23a); }
  .photo--jelly { left: 404px; top: 108px; transform: rotate(-2deg); }
  .photo--jelly .photo__fill { background: linear-gradient(180deg, #1a1a1a 15%, var(--jelly-tone-a) 45%, var(--jelly-tone-b) 75%, #1a1a1a); }

  .owner-name {
    position: absolute; left: 26px; top: 193px;
    font-weight: 600; font-size: 52px; line-height: 1; color: var(--paper);
  }
  .contact { position: absolute; left: 26px; list-style: none; font-size: 18.5px; font-weight: 600; }
  .contact li { display: flex; align-items: center; gap: 9px; height: 23px; white-space: nowrap; }
  .contact { top: 264px; }
  .contact__icon { width: 21px; height: 21px; flex: none; }
  .contact__square { width: 19px; height: 19px; background: var(--ink); border-radius: 3px; flex: none; margin: 0 1px; }
</style>
</head>
<body>
<main class="canvas">

  <section class="card card--front" aria-label="Business card front">
    <div class="card__face">
      <div class="logo-tile"></div>
      <h1 class="brand-name">Plain Kettle Show</h1>
      <p class="tagline">I'll see you next time, for my next meal</p>

      <figure class="photo photo--cake">
        <div class="photo__fill" role="img" aria-label="Photo of a rainbow layer cake covered in candy"></div>
      </figure>
      <figure class="photo photo--jelly">
        <div class="photo__fill" role="img" aria-label="Photo of a slice of rainbow layered jelly"></div>
      </figure>

      <p class="owner-name">Marcus</p>
      <ul class="contact">
        <li>
          <svg class="contact__icon" viewBox="0 0 21 21" aria-hidden="true">
            <rect x="1" y="7" width="19" height="13" rx="1.5" fill="#231f1a"/>
            <path d="M1.5 8 L10.5 14.5 L19.5 8" fill="none" stroke="#f79d21" stroke-width="1.6"/>
            <path d="M10.5 1 V9 M7 5.5 L10.5 9 L14 5.5" fill="none" stroke="#231f1a" stroke-width="2"/>
          </svg>
          promos@zentaclip.example
        </li>
        <li>
          <span class="contact__square"></span>
          www.streamora.example/user/PlainKettleShow
        </li>
      </ul>
    </div>
  </section>

  <section class="card card--back" aria-label="Business card back">
    <div class="card__face">
      <div class="logo-tile"></div>
      <h2 class="brand-name">Plain Kettle Show</h2>
      <p class="tagline">I'll see you next time, for my next meal</p>
    </div>
  </section>

</main>
</body>
</html>
```